Artwork for Band Promotional Material

We are a new band that is trying to make a primary image/logo for marketing and sharing purposes. The goal is to have an image that stands out, is interesting, creative and unique. The band name is Velvet Lanternfall, which can be feature or not feature in the artwork, if the image is interesting to begin with its ok if there is no name. Or feel free to incorporate the name in a unique way.
Velvet means the idea of Perfection. What is the cause of the idea of perfection in an imperfect world. To me, perfection is unnatural and pursuit of perfection in some regards, can be pathological unless one knows their limitations, so, if there is a cure for this, there must also be a Cause.
Our style of music is hopefull yet dark with ambiance. There is some hip hop, but its smokey and chill. Its powerfully feminine. We are a two piece incorporating guitar, piano and 70's synthesizers. Our music and sounds have been described as sounding like they are from the 30s - 50s with a modern twist.
Ideally, the image would be somewhat abstract and have a 20s-30s silent film feel but with some color. It should imply some loneliness but also hopefulness. Darkness in light.
To be totally honest, we want the image to be like our music, unclassifiable and unique but grab the attention of the person looking.
This image will be used for all marketing and promotional material.
I placed some images I use currently for our songs we share with people. We love some darkness in the image as well as a sense of surrealism.
I included on song, an ambient version and the "Single" version of a song, if you want to get a vibe. We also play blues (our own blues so to speak).
Here is a link to an mages I like and the 'vibe" The first three on the page and Hollow Meridian (my fav). But, like I said, I am open to anything and am looking something unique.
http://www.quietdriftjournal.example/
Target Market(s)
Music Lovers, particularly those who enjoy artful music and art.
Industry/Entity Type
Music Download
Requirements
Must have
- Creative
- Element of surrealism
- Darkness with some hopefullness
- Something subdued but with a striking imaging (ie, not too busy or over the top)
Nice to have
- The band Name - Velvet Lanternfall (or just Velvet) but not a necessity, feel free to be creative with it.
- 20-30s silent film/horror movie type vibe but simple
- Some simple color, can be desaturated
- Lower on the Nice to Have List
- Incorporating a Piano/guitar in an abstract way is a nice touch, but not required by any means.
- very subtle, extremely subtle religious connotation is always interesting (we are not a religious band, but something that is part of our history) but, it would have to be subtle and not a 'pro-religious' or religious advertisement, but religious imagery, particularly gothic would be interesting, but not needed.
Should not have
- Nothing cartoonish or humorous, unless dark satire.

```html
<!DOCTYPE html>
<html lang="en">
<head>
<meta charset="UTF-8">
<title>Velvet</title>
<link rel="stylesheet" href="https://fonts.googleapis.com/css2?family=Arimo:wght@400&display=swap">
<style>
  :root {
    --bg: #1b1b1b;
    --ink: #8b8b8b;
    --rule: #8d8d8d;
    --photo-glow: #a8a8a8;
    --photo-light: #858585;
    --photo-mid: #555555;
    --photo-shadow: #2e2e2e;
    --photo-dark: #0c0c0c;
  }
  * { margin: 0; padding: 0; box-sizing: border-box; }
  html, body {
    width: 1200px;
    height: 1200px;
    overflow: hidden;
    background: var(--bg);
  }
  .cover {
    position: relative;
    width: 1200px;
    height: 1200px;
    background: var(--bg);
    overflow: hidden;
  }
  .band-name {
    position: absolute;
    left: 80px;
    top: 58px;
    font-family: "Arimo", Arial, sans-serif;
    font-weight: 400;
    font-size: 82px;
    line-height: 1;
    letter-spacing: -3px;
    color: var(--ink);
  }
  .divider {
    position: absolute;
    left: 385px;
    top: 494px;
    width: 363px;
    height: 10px;
    background: var(--rule);
  }
  .window-photo {
    position: absolute;
    left: 637px;
    top: 569px;
    width: 370px;
    height: 387px;
    overflow: hidden;
    background:
      radial-gradient(ellipse 28% 22% at 22% 42%, rgba(190,190,190,0.55) 0%, rgba(190,190,190,0) 100%),
      radial-gradient(ellipse 26% 24% at 62% 36%, rgba(200,200,200,0.5) 0%, rgba(200,200,200,0) 100%),
      radial-gradient(ellipse 20% 30% at 90% 30%, rgba(170,170,170,0.4) 0%, rgba(170,170,170,0) 100%),
      radial-gradient(ellipse 30% 14% at 50% 90%, rgba(230,230,230,0.35) 0%, rgba(230,230,230,0) 100%),
      radial-gradient(ellipse 22% 12% at 90% 88%, rgba(230,230,230,0.3) 0%, rgba(230,230,230,0) 100%),
      linear-gradient(180deg,
        var(--photo-mid) 0%,
        var(--photo-light) 30%,
        var(--photo-glow) 42%,
        var(--photo-mid) 56%,
        var(--photo-shadow) 68%,
        var(--photo-dark) 82%,
        var(--photo-dark) 100%);
  }
  .photo-grain {
    position: absolute;
    inset: 0;
    width: 100%;
    height: 100%;
    opacity: 0.35;
    mix-blend-mode: overlay;
  }
  .grain {
    position: absolute;
    inset: 0;
    width: 1200px;
    height: 1200px;
    pointer-events: none;
    opacity: 0.16;
    mix-blend-mode: screen;
  }
</style>
</head>
<body>
  <main class="cover">
    <h1 class="band-name">velvet</h1>
    <div class="divider"></div>
    <div class="window-photo" role="img" aria-label="Grainy black and white night photograph of a ceiling with beams above a row of lit paned windows">
      <svg class="photo-grain" viewBox="0 0 370 387" preserveAspectRatio="none" aria-hidden="true">
        <filter id="photo-noise">
          <feTurbulence type="fractalNoise" baseFrequency="1.1" numOctaves="2" stitchTiles="stitch"/>
          <feColorMatrix type="saturate" values="0"/>
        </filter>
        <rect width="370" height="387" filter="url(#photo-noise)"/>
      </svg>
    </div>
    <svg class="grain" viewBox="0 0 1200 1200" aria-hidden="true">
      <filter id="film-grain">
        <feTurbulence type="fractalNoise" baseFrequency="0.9" numOctaves="2" stitchTiles="stitch"/>
        <feColorMatrix type="saturate" values="0"/>
      </filter>
      <rect width="1200" height="1200" filter="url(#film-grain)" opacity="0.5"/>
    </svg>
  </main>
</body>
</html>
```